Create a Graphic About YOURSELF and PixelHarbor

PixelHarbor would like you (designers) to create an awesome graphic to promote YOURSELF and your profile on PixelHarbor!

Your graphic should communicate your name, your services and should mention PixelHarbor.

The design should be perfect for sharing on Chatterly. Here's an example of what we'd like http://blog.pixelharbor-example.ca/article/333/pixelharbor-launches-3000-hire-me-social-design-contest

Once you submitted your design, we'd love you to share the design ('advertisement') and promote yourself and PixelHarbor to your friends and potential customers. So make your submissions great and get your friends to vote for your design by 'Liking' it on Chatterly!

Prizes:
$1500 - "PixelHarbor Community" prize awarded to the designer with the most Chatterly 'Likes'
5 x $50 for the next 5 'most liked' designs on Chatterly

$1000 - "Hire Me" prize awarded to the designer who receives the most client invites
5 x $50 for the next 5 'most invited' designers

In summary, this is a great opportunity for you to increase your exposure to PixelHarbor customers and win cash prizes. Show off your design skills and get hired by PixelHarbor customers from around the world!

Target Market(s)

Fans, friends and customers of YOU

Industry/Entity Type

Cash

Requirements
Must have
• 1) Include your PixelHarbor user name on the graphic so customers can find you in the PixelHarbor Designer Directory
2) Include the tagline "Hire Me on PixelHarbor.com!" in your graphic design.
3) Share your design's URL on our Chatterly wall at http://chatterly-example.com/pixelharbor and get your friends to 'like' your design.
Nice to have
• 1) Include a tagline that expresses your design approach/philosophy
2) Artwork dimensions: 403 x 403 px
3) You can submit more than 1 design!
Should not have
• You must own the copyright of any images you use including stock imagery.

```html
<!DOCTYPE html>
<html lang="en">
<head>
<meta charset="utf-8">
<title>Hire Me – MV, illustrator &amp; graphic designer</title>
<link rel="stylesheet" href="https://fonts.googleapis.com/css2?family=Reenie+Beanie&family=Nothing+You+Could+Do&display=swap">
<style>
  :root {
    --page: #ffffff;
    --burlap-light: #d9c48f;
    --burlap-mid: #b79b5c;
    --burlap-burnt: #5a4218;
    --ink: #2b2212;
    --splash: #d41414;
    --splash-dark: #a80c0c;
    --chalk: #ffffff;
  }
  html, body {
    margin: 0;
    padding: 0;
    width: 1200px;
    height: 1200px;
    overflow: hidden;
    background: var(--page);
  }
  .hire-card {
    position: relative;
    width: 1200px;
    height: 1200px;
  }
  .hire-card__art {
    position: absolute;
    inset: 0;
  }
  .hire-card__text {
    position: absolute;
    margin: 0;
    white-space: nowrap;
    line-height: 1;
  }
  .hire-card__heading {
    left: 140px;
    top: 235px;
    font-family: "Reenie Beanie", cursive;
    font-size: 150px;
    color: var(--ink);
    letter-spacing: 4px;
  }
  .hire-card__on {
    left: 125px;
    top: 840px;
    font-family: "Reenie Beanie", cursive;
    font-size: 130px;
    color: var(--ink);
  }
  .hire-card__site {
    left: 110px;
    top: 925px;
    font-family: "Reenie Beanie", cursive;
    font-size: 150px;
    color: var(--ink);
    letter-spacing: 6px;
  }
  .hire-card__initials {
    left: 735px;
    top: 415px;
    font-family: "Nothing You Could Do", cursive;
    font-size: 120px;
    color: var(--chalk);
  }
  .hire-card__role {
    font-family: "Nothing You Could Do", cursive;
    color: var(--chalk);
  }
  .hire-card__role--first {
    left: 635px;
    top: 580px;
    font-size: 64px;
  }
  .hire-card__role--second {
    left: 615px;
    top: 660px;
    font-size: 58px;
  }
</style>
</head>
<body>
<main class="hire-card">
  <svg class="hire-card__art" width="1200" height="1200" viewBox="0 0 1200 1200" xmlns="http://www.w3.org/2000/svg">
    <defs>
      <radialGradient id="burlap-tone" cx="50%" cy="50%" r="60%">
        <stop offset="0%" stop-color="var(--burlap-light)"/>
        <stop offset="70%" stop-color="var(--burlap-mid)"/>
        <stop offset="100%" stop-color="var(--burlap-burnt)"/>
      </radialGradient>
      <radialGradient id="splash-tone" cx="50%" cy="45%" r="55%">
        <stop offset="0%" stop-color="var(--splash)"/>
        <stop offset="100%" stop-color="var(--splash-dark)"/>
      </radialGradient>
    </defs>
    <path class="hire-card__burlap" role="img" aria-label="Woven burlap fabric texture with scorched, wavy edges"
      fill="url(#burlap-tone)"
      d="M50 40 Q110 25 170 40 T290 40 T410 40 T530 40 T650 40 T770 40 T890 40 T1010 40 T1150 35
         Q1165 100 1150 160 T1150 280 T1150 400 T1150 520 T1150 640 T1150 760 T1150 880 T1150 1000 T1160 1160
         Q1090 1175 1030 1160 T910 1160 T790 1160 T670 1160 T550 1160 T430 1160 T310 1160 T190 1160 T45 1165
         Q30 1100 45 1040 T45 920 T45 800 T45 680 T45 560 T45 440 T45 320 T45 200 T50 40 Z"/>
    <path class="hire-card__splash" role="img" aria-label="Red paint splatter"
      fill="url(#splash-tone)"
      d="M850 390 C960 385 1075 470 1080 590 C1090 720 990 830 860 835 C720 845 600 760 590 630
         C580 500 700 395 850 390 Z"/>
  </svg>

  <p class="hire-card__text hire-card__heading">hire me</p>
  <p class="hire-card__text hire-card__initials">MV</p>
  <p class="hire-card__text hire-card__role hire-card__role--first">illustrator</p>
  <p class="hire-card__text hire-card__role hire-card__role--second">graphic designer</p>
  <p class="hire-card__text hire-card__on">on</p>
  <p class="hire-card__text hire-card__site">www.pixelharbor.com</p>
</main>
</body>
</html>
```